Industrial Company Profile Brochure Design

We need company profile brochure design. We are in industrial valve business and we are serving oil, petrochemical and power plants. We are working with our clients as trusted advisor. So, the final design should communicate valve solutions expert. The brochure should be 4 pages (including front and back) or folded style. However, it is open. We do not like to put any restriction on creativity. We leave the decision for number of pages and page size to the designer. The color theme should be same as / compatible with logo colors. You should use icons.Find attached the followings:- Our Logo- Word file that contains the required content (text and photos) for the brochure.3 Modern brochure designs. We like these designs. This is just to give you idea about what we like. The brochure is simple, clear and easy to get full information quickly.- Just banner for valve and components. You may need it.

Target Market(s)

The end users of oi, petrochemical and power plants

Industry/Entity Type

Engineering Consulting

Requirements
Must have
• - You must add our slogan. It is "Your Valves Solutions Expert"

```html
<!DOCTYPE html>
<html lang="en">
<head>
<meta charset="utf-8">
<title>Korvan Valves – Company Profile</title>
<link href="https://fonts.googleapis.com/css2?family=Montserrat:wght@400;500;600;700&display=swap" rel="stylesheet">
<style>
  :root {
    --orange: #f39420;
    --orange-soft: #f6b25e;
    --grey: #8a8a8a;
    --grey-light: #bdbdbd;
    --ink: #2f2f2f;
    --paper: #f4f4f4;
    --stage: #3a3a3a;
  }
  * { margin: 0; padding: 0; box-sizing: border-box; }
  html, body { width: 1200px; height: 824px; overflow: hidden; }
  body {
    background: var(--stage);
    font-family: "Montserrat", sans-serif;
    color: var(--ink);
    position: relative;
  }
  .spread {
    position: absolute;
    left: 90px; top: 52px;
    width: 1020px; height: 720px;
    display: flex;
  }
  .page {
    position: relative;
    width: 510px; height: 720px;
    background: var(--paper);
    overflow: hidden;
  }
  .page--back { border-right: 1px solid #dcdcdc; }

  /* back page */
  .back-decor {
    position: absolute; left: 0; top: 40px;
    width: 120px; height: 300px;
  }
  .why-us { position: absolute; left: 150px; top: 70px; width: 320px; }
  .section-title {
    font-size: 17px; font-weight: 600; letter-spacing: 1px;
    margin-bottom: 18px;
  }
  .accent { color: var(--orange); }
  .feature { margin-bottom: 22px; }
  .feature h3 {
    color: var(--orange); font-size: 13px; font-weight: 500;
    margin-bottom: 6px;
  }
  .feature p { font-size: 8.5px; line-height: 1.55; color: #444; }

  .contact { position: absolute; left: 150px; top: 400px; width: 320px; }
  .contact .section-title { margin-bottom: 12px; }
  .contact-name { font-size: 11px; font-weight: 500; margin-bottom: 6px; }
  .contact-list { list-style: none; }
  .contact-list li {
    display: flex; align-items: center; gap: 8px;
    font-size: 10.5px; margin-bottom: 5px;
  }
  .contact-list svg { width: 11px; height: 11px; flex: none; }

  .partners { position: absolute; left: 150px; top: 575px; width: 320px; }
  .partners .section-title { margin-bottom: 16px; }
  .partner-row { display: flex; align-items: center; gap: 26px; }
  .partner-badge { height: 16px; width: 58px; background: var(--grey-light); border-radius: 3px; }
  .partner-badge--round { width: 26px; height: 26px; border-radius: 50%; background: #1b1b1b; }

  /* front cover */
  .cover-decor {
    position: absolute; left: 50px; top: 0;
    width: 460px; height: 360px;
    background: linear-gradient(135deg, var(--orange) 0%, var(--orange-soft) 45%, var(--grey) 100%);
    border-bottom-left-radius: 230px;
    border-bottom-right-radius: 40px;
    opacity: 0.9;
  }
  .brand { position: absolute; left: 50px; top: 445px; display: flex; align-items: center; gap: 10px; }
  .brand-dot { width: 22px; height: 22px; border-radius: 50%; background: var(--orange); }
  .brand-name { font-size: 26px; font-weight: 700; color: var(--orange); line-height: 1; }
  .brand-sub { position: absolute; left: 82px; top: 478px; font-size: 13px; font-weight: 600; color: var(--grey); }
  .doc-type {
    position: absolute; left: 50px; top: 560px;
    font-size: 13px; font-weight: 600; letter-spacing: 1.5px; color: #555;
  }
  .slogan {
    position: absolute; right: 40px; top: 390px;
    text-align: right; font-size: 22px; font-weight: 500;
    line-height: 1.15; letter-spacing: 1px; text-transform: uppercase;
  }
  .slogan .accent { font-weight: 600; }
  .web-band {
    position: absolute; right: 0; top: 510px;
    width: 180px; height: 26px;
    background: var(--orange);
    border-left: 5px solid var(--grey);
    color: #fff; font-size: 10px;
    display: flex; align-items: center; justify-content: center;
  }
</style>
</head>
<body>
  <main class="spread">
    <section class="page page--back">
      <div class="back-decor" role="img" aria-label="Decorative orange and grey arc motif" style="background:linear-gradient(180deg,var(--orange) 0%,var(--grey-light) 60%,var(--grey) 100%);border-top-right-radius:120px;border-bottom-right-radius:120px;opacity:.85"></div>

      <div class="why-us">
        <h2 class="section-title">WHY <span class="accent">US</span></h2>
        <div class="feature">
          <h3>Quality Control</h3>
          <p>Our quality control processes, implemented across all stages of valve solutions development, help in keeping our solutions highly reliable and accurate for long-term implementations.</p>
        </div>
        <div class="feature">
          <h3>Customer Satisfaction</h3>
          <p>Our teams are committed to handling the needs of our customers in a timely manner, keeping them satisfied and happy. This also makes us a reliable choice for any kind of upgrade or replacement parts in an emergency situation.</p>
        </div>
        <div class="feature">
          <h3>Highly Affordable</h3>
          <p>Our awareness of the latest technologies and unique methods assists us in providing solutions with lower costs; we make sure to pass on this advantage to our clients by keeping our services highly affordable for them.</p>
        </div>
      </div>

      <div class="contact">
        <h2 class="section-title">CONTACT <span class="accent">DETAILS:</span></h2>
        <p class="contact-name">Korvan Valves</p>
        <ul class="contact-list">
          <li><svg viewBox="0 0 12 12"><path d="M3 1l2 2-1 1.5a6 6 0 0 0 3.5 3.5L9 7l2 2-1.5 2A9 9 0 0 1 1 2.5z" fill="none" stroke="#f39420" stroke-width="1"/></svg>+000 555 014 2200</li>
          <li><svg viewBox="0 0 12 12"><path d="M6 11s-4-4-4-6.5a4 4 0 0 1 8 0C10 7 6 11 6 11z" fill="none" stroke="#f39420" stroke-width="1"/><circle cx="6" cy="4.5" r="1.3" fill="#f39420"/></svg>Harbor Rd - Eastport | 10101</li>
          <li><svg viewBox="0 0 12 12"><rect x="1" y="2.5" width="10" height="7" fill="none" stroke="#f39420" stroke-width="1"/><path d="M1 2.5l5 4 5-4" fill="none" stroke="#f39420" stroke-width="1"/></svg>info@korvanvalves.com</li>
          <li><svg viewBox="0 0 12 12"><circle cx="6" cy="6" r="5" fill="none" stroke="#f39420" stroke-width="1"/><path d="M1 6h10M6 1c2 2 2 8 0 10M6 1c-2 2-2 8 0 10" fill="none" stroke="#f39420" stroke-width=".8"/></svg>www.korvanvalves.com</li>
        </ul>
      </div>

      <div class="partners">
        <h2 class="section-title">PARTNERS:</h2>
        <div class="partner-row">
          <span class="partner-badge" style="background:var(--orange)"></span>
          <span class="partner-badge" style="background:#d2232a"></span>
          <span class="partner-badge" style="background:#1e4f9c"></span>
          <span class="partner-badge partner-badge--round"></span>
        </div>
      </div>
    </section>

    <section class="page page--front">
      <div class="cover-decor" role="img" aria-label="Large decorative orange and grey graphic"></div>

      <div class="brand">
        <span class="brand-dot"></span>
        <span class="brand-name">KORVAN</span>
      </div>
      <p class="brand-sub">Valves</p>

      <h1 class="slogan">Your<br>Valves<br>Solutions<br><span class="accent">Expert</span></h1>
      <div class="web-band">www.korvanvalves.com</div>

      <p class="doc-type">COMPANY PROFILE</p>
    </section>
  </main>
</body>
</html>
```